Can you make our site AWESOME?

Hi Guys,

I am a co-founder of Tipper Crate Rentals Australia, the world's first e-commerce skip bin business.

We are looking to update our site before a launch into the UK in March.

Please help us by submitting your designs for the following pages:

- Home page (www.tippercraterentals-example.com.au)
- About us (https://www.tippercraterentals-example.com.au/pages/about-us
- Contact us (https://www.tippercraterentals-example.com.au/pages/contact-us)
- Quick Quote / Pricing (https://www.tippercraterentals-example.com.au/pages/free-instant-quote-skip-bin-hire)

NOTES:
- Design should be high-converting
- best designs will be fresh, modern, easy to read, distinctive and memorable
- please use our logo and video colours
- feel free to change logos, layout, images and anything else you feel can be improved
- the winning designer will potentially have the opportunity to re-design the other pages on our site
- brief is for design only

Any questions just ask.

Thanks,
Oliver

```html
<!DOCTYPE html>
<html lang="en">
<head>
<meta charset="utf-8">
<title>Tipper Crate Rentals Australia</title>
<link rel="stylesheet" href="https://fonts.googleapis.com/css2?family=Poppins:wght@300;400;500;600;700&display=swap">
<style>
:root{
  --purple:#5a5e9e;
  --purple-dark:#3f437e;
  --purple-light:#8e92c4;
  --navy:#2c2f63;
  --green:#3cb85a;
  --green-dark:#2e9c4a;
  --ink:#333;
  --muted:#666;
  --grey-bg:#f4f4f7;
  --footer:#363636;
  --footer-bottom:#262626;
  --white:#fff;
}
*{box-sizing:border-box;margin:0;padding:0}
html,body{width:1200px;height:3734px;overflow:hidden}
body{font-family:"Poppins",sans-serif;color:var(--ink);background:var(--white);position:relative}
.abs{position:absolute}
.center{text-align:center}

/* header */
.site-header{position:absolute;left:0;top:0;width:1200px;height:90px;background:var(--white);z-index:2}
.brand{position:absolute;left:88px;top:22px;display:flex;align-items:center;gap:10px}
.brand-square{width:34px;height:34px;background:var(--green);border-radius:4px}
.brand-name{font-weight:700;font-size:15px;color:var(--navy);line-height:1.1;width:200px}
.main-nav{position:absolute;left:405px;top:28px;display:flex;gap:44px;font-size:12.5px;font-weight:500;color:var(--navy)}
.call-btn{position:absolute;left:920px;top:0;width:190px;height:34px;background:var(--purple);color:#fff;font-size:12px;font-weight:600;border-radius:0 0 8px 8px;display:flex;align-items:center;justify-content:center}
.login{position:absolute;left:920px;top:46px;width:190px;text-align:center;font-size:11px;font-weight:600;color:var(--green)}

/* hero */
.hero{position:absolute;left:0;top:90px;width:1200px;height:610px;background:linear-gradient(180deg,var(--purple) 0%,#6f73ae 55%,#7b7fb8 100%);overflow:hidden}
.hero-skyline{position:absolute;left:0;top:330px;width:1200px;height:280px;background:linear-gradient(180deg,rgba(63,67,126,0) 0%,rgba(63,67,126,.55) 40%,var(--purple-dark) 100%)}
.hero h1{position:absolute;top:88px;width:1200px;text-align:center;color:#fff;font-size:44px;font-weight:600}
.hero .tagline{position:absolute;top:160px;width:1200px;text-align:center;color:#e6e7f6;font-size:20px;font-weight:300}
.label{font-size:13px;font-weight:600;color:#fff;text-align:center}
.search{position:absolute;height:56px;display:flex;border-radius:28px;overflow:hidden;background:#fff}
.search .field{flex:1;padding-left:30px;display:flex;align-items:center;font-size:14px;color:#999}
.search .go{width:124px;background:var(--green);color:#fff;font-size:12px;font-weight:600;display:flex;align-items:center;justify-content:center;gap:8px}
.hero-curve{position:absolute;left:0;top:640px;width:1200px;height:70px}

.categories{position:absolute;left:165px;top:558px;display:flex;gap:18px;z-index:2}
.cat-card{width:160px;height:158px;background:#fff;border-radius:6px;box-shadow:0 6px 18px rgba(0,0,0,.12);display:flex;flex-direction:column;align-items:center;justify-content:flex-end;padding-bottom:22px}
.cat-icon{width:54px;height:46px;margin-bottom:22px}
.cat-card span{font-size:11px;font-weight:600;color:var(--navy);letter-spacing:.5px}

/* rated + video */
.rated{position:absolute;top:772px;width:1200px;text-align:center;font-size:27px;font-weight:300;color:var(--navy);line-height:1.35}
.grey-wave{position:absolute;left:0;top:1180px;width:1200px;height:660px;background:var(--grey-bg)}
.video{position:absolute;left:240px;top:882px;width:737px;height:393px;background:linear-gradient(180deg,#7478b2 0%,#8f93c6 55%,#5f9a5a 85%,#58945a 100%);box-shadow:0 6px 20px rgba(0,0,0,.18);z-index:2}
.play{position:absolute;left:330px;top:160px;width:78px;height:78px;border-radius:50%;background:#fff;display:flex;align-items:center;justify-content:center}

/* steps */
.section-title{position:absolute;width:1200px;text-align:center;font-weight:300;color:var(--navy)}
.steps{position:absolute;left:78px;top:1485px;display:flex;gap:22px}
.step{width:334px;height:150px;background:#fff;border:1px solid #e6e6ec;box-shadow:0 3px 10px rgba(0,0,0,.05);position:relative;padding:14px 10px 0 86px}
.step .icon{position:absolute;left:20px;top:18px;width:52px;height:52px}
.step .num{position:absolute;left:36px;top:86px;font-size:48px;font-weight:600;color:#e8e8ee}
.step h3{font-size:17.5px;font-weight:600;color:var(--navy);margin-bottom:6px;white-space:nowrap}
.step p{font-size:12px;line-height:1.6;color:var(--ink)}
.step p b{color:var(--green);font-weight:500}
.manage{position:absolute;top:1738px;width:1200px;text-align:center;font-size:19px;color:var(--navy);line-height:1.5}

/* testimonials */
.reviews{position:absolute;left:0;top:1840px;width:1200px;height:700px;background:linear-gradient(180deg,var(--purple) 0%,#6f73ae 45%,#b9bbdc 80%,#fff 100%)}
.review{position:absolute;top:165px;width:322px;height:410px;background:#fff;box-shadow:0 4px 16px rgba(0,0,0,.08);padding:78px 52px 0 52px}
.review .quote{position:absolute;left:24px;top:-18px;width:26px;height:46px;background:#fff;border-radius:14px 14px 4px 14px}
.review p{font-size:12px;line-height:2.1;color:#555}
.review hr{border:0;border-top:1px solid #eee;margin:22px 0 26px}
.reviewer{display:flex;align-items:center;gap:12px;font-size:14px;color:var(--green)}
.avatar{width:30px;height:30px;border-radius:50%;background:#c9a98d}
.dots{position:absolute;top:2452px;left:590px;display:flex;gap:5px}
.dots i{width:6px;height:6px;border-radius:50%;background:#c9cbe3}
.dots i.on{background:var(--purple)}

/* benefits */
.benefits{position:absolute;left:50px;top:2670px;display:flex;gap:0}
.benefit{width:275px;text-align:center;padding:0 22px}
.benefit .icon{width:66px;height:50px;margin:0 auto 18px}
.benefit h4{font-size:14px;font-weight:600;color:var(--navy);margin-bottom:10px}
.benefit p{font-size:11.5px;line-height:1.75;color:#555}

/* cta */
.cta{position:absolute;left:0;top:2963px;width:1200px;height:420px;background:linear-gradient(180deg,var(--purple) 0%,#6b6fab 100%);overflow:hidden}
.cta-skyline{position:absolute;left:0;top:120px;width:1200px;height:300px;background:linear-gradient(180deg,rgba(63,67,126,0),rgba(63,67,126,.6))}
.cta h2{position:absolute;top:65px;width:1200px;text-align:center;color:#fff;font-size:32px;font-weight:600}
.cta .sub{position:absolute;top:118px;width:1200px;text-align:center;color:#e6e7f6;font-size:15px}

/* footer */
.footer-wave{position:absolute;left:0;top:3300px;width:1200px;height:100px}
.site-footer{position:absolute;left:0;top:3390px;width:1200px;height:232px;background:var(--footer);color:#e8e8e8;font-size:11.5px}
.foot-col{position:absolute;top:20px;line-height:2.2}
.news h5{font-size:11.5px;font-weight:500;line-height:1.6}
.subscribe{position:absolute;left:715px;top:86px;width:358px;height:44px;border-radius:22px;overflow:hidden;display:flex;background:#fff}
.subscribe .field{flex:1;padding-left:22px;display:flex;align-items:center;color:#777;font-size:12px}
.subscribe .go{width:130px;background:var(--green);color:#fff;font-weight:600;display:flex;align-items:center;justify-content:center;font-size:12px}
.socials{position:absolute;left:722px;top:158px;display:flex;gap:34px}
.socials i{width:14px;height:14px;border-radius:50%;background:#cfcfcf}
.foot-bottom{position:absolute;left:0;top:3622px;width:1200px;height:112px;background:var(--footer-bottom);color:#ddd;font-size:11px}
.pay{position:absolute;left:846px;top:34px;display:flex;gap:16px}
.pay i{width:36px;height:22px;border-radius:3px;background:#bdbdbd}
</style>
</head>
<body>

<header class="site-header">
  <div class="brand"><div class="brand-square"></div><div class="brand-name">Tipper Crate Rentals Australia</div></div>
  <nav class="main-nav"><span>PRICING</span><span>LEARN MORE</span><span>ABOUT</span><span>TRADE SECRETS</span><span>CONTACT</span></nav>
  <div class="call-btn">CALL NOW: 1800 000 111</div>
  <div class="login">LOGIN / CREATE ACCOUNT</div>
</header>

<section class="hero">
  <div class="hero-skyline" role="img" aria-label="City skyline silhouette"></div>
  <h1>1000's of Skips at Your Finger Tips</h1>
  <div class="tagline">Best Service &amp; Price | Hassle Free | Australia Wide</div>
  <div class="label abs" style="top:228px;width:1200px">Instant Quote</div>
  <div class="search" style="left:320px;top:278px;width:562px">
    <div class="field">Enter postcode or suburb</div>
    <div class="go"><svg width="12" height="12" viewBox="0 0 12 12"><circle cx="5" cy="5" r="3.6" fill="none" stroke="#fff" stroke-width="1.8"/><path d="M8 8l3 3" stroke="#fff" stroke-width="1.8"/></svg>SEARCH</div>
  </div>
</section>
<svg class="hero-curve" viewBox="0 0 1200 70" preserveAspectRatio="none"><path d="M0 50 Q600 -20 1200 50 L1200 70 L0 70Z" fill="#fff"/></svg>

<div class="categories">
  <div class="cat-card"><svg class="cat-icon" viewBox="0 0 54 46"><path d="M6 22L27 4l21 18" fill="none" stroke="var(--green)" stroke-width="3"/><rect x="12" y="20" width="30" height="24" fill="none" stroke="var(--green)" stroke-width="3"/></svg><span>RENOVATOR</span></div>
  <div class="cat-card"><svg class="cat-icon" viewBox="0 0 54 46"><rect x="8" y="24" width="38" height="18" rx="3" fill="none" stroke="var(--green)" stroke-width="3"/><path d="M20 24V8h14v16" fill="none" stroke="var(--green)" stroke-width="3"/></svg><span>TRADIE</span></div>
  <div class="cat-card"><svg class="cat-icon" viewBox="0 0 54 46"><rect x="8" y="6" width="38" height="34" fill="none" stroke="var(--green)" stroke-width="3"/><path d="M14 32l10-12 8 8 8-10" fill="none" stroke="var(--green)" stroke-width="3"/></svg><span>BUILDER</span></div>
  <div class="cat-card"><svg class="cat-icon" viewBox="0 0 54 46"><rect x="6" y="14" width="42" height="28" rx="3" fill="none" stroke="var(--green)" stroke-width="3"/><path d="M20 14V6h14v8M6 26h42" fill="none" stroke="var(--green)" stroke-width="3"/></svg><span>CORPORATE</span></div>
  <div class="cat-card"><svg class="cat-icon" viewBox="0 0 54 46"><rect x="8" y="10" width="16" height="32" fill="none" stroke="var(--green)" stroke-width="3"/><rect x="28" y="4" width="18" height="38" fill="none" stroke="var(--green)" stroke-width="3"/></svg><span>NATIONAL</span></div>
</div>

<div class="grey-wave"></div>
<svg class="abs" style="left:0;top:1170px" width="1200" height="60" viewBox="0 0 1200 60" preserveAspectRatio="none"><path d="M0 20 Q600 -10 1200 40 L1200 60 L0 60Z" fill="var(--grey-bg)"/></svg>

<div class="rated">Australia's Highest Rated Skip Bin<br>Hire Company - Rated by You</div>
<div class="video" role="img" aria-label="Animated explainer video still: a homeowner outside his house wondering where his skip bin is">
  <div class="play"><svg width="24" height="26" viewBox="0 0 24 26"><path d="M4 2l18 11L4 24z" fill="var(--navy)"/></svg></div>
</div>

<div class="section-title" style="top:1390px;font-size:30px">As Easy As 1, 2, 3...</div>
<div class="steps">
  <div class="step">
    <svg class="icon" viewBox="0 0 52 52"><rect x="4" y="6" width="32" height="26" rx="4" fill="none" stroke="var(--green)" stroke-width="2.5"/><path d="M12 32l-4 10 12-10" fill="none" stroke="var(--green)" stroke-width="2.5"/><text x="20" y="26" font-size="18" font-family="Poppins" fill="var(--navy)" text-anchor="middle">?</text></svg>
    <div class="num">1</div>
    <h3>Simple, Easy Booking</h3>
    <p>Call <b>1800 000 111</b> or <b>click here</b> to get started with your instant quote</p>
  </div>
  <div class="step">
    <svg class="icon" viewBox="0 0 52 52"><rect x="6" y="4" width="28" height="38" rx="2" fill="none" stroke="var(--navy)" stroke-width="2.5"/><circle cx="36" cy="36" r="11" fill="var(--green)"/><path d="M31 36l4 4 7-8" fill="none" stroke="#fff" stroke-width="2.5"/></svg>
    <div class="num">2</div>
    <h3>Instant Confirmation</h3>
    <p>Receive your booking details and a 30 minute courtesy call before drop off</p>
  </div>
  <div class="step">
    <svg class="icon" viewBox="0 0 52 52"><path d="M6 20l20-10 20 10v20L26 50 6 40z" fill="none" stroke="var(--green)" stroke-width="2.5"/><path d="M6 20l20 10 20-10M26 30v20" fill="none" stroke="var(--green)" stroke-width="2.5"/></svg>
    <div class="num">3</div>
    <h3>Gone When Your Ready!</h3>
    <p>Let us know and your bin will be gone within 24hrs</p>
  </div>
</div>
<div class="manage">We manage your booking from start to finish,<br>so you can focus on other things</div>

<section class="reviews">
  <div class="section-title" style="top:58px;font-size:30px;color:#fff">Five Star Service</div>
  <div class="review" style="left:92px"><div class="quote"></div><p>There are many variations of passages of available but the majority have suffer alteration in some form by inject humour or random words which don't look even slightly believe you are going middle of text.</p><hr><div class="reviewer"><div class="avatar"></div>Daniel Hart</div></div>
  <div class="review" style="left:443px"><div class="quote"></div><p>There are many variations of passages of available but the majority have suffer alteration in some form by inject humour or random words which don't look even slightly believe you are going middle of text.</p><hr><div class="reviewer"><div class="avatar"></div>Megan Reilly</div></div>
  <div class="review" style="left:797px"><div class="quote"></div><p>There are many variations of passages of available but the majority have suffer alteration in some form by inject humour or random words which don't look even slightly believe you are going middle of text.</p><hr><div class="reviewer"><div class="avatar"></div>Grant Pellow</div></div>
</section>
<div class="dots"><i class="on"></i><i></i><i></i></div>

<div class="section-title" style="top:2555px;font-size:30px">Save Time. Save Money.</div>
<div class="benefits">
  <div class="benefit"><svg class="icon" viewBox="0 0 66 50"><rect x="4" y="16" width="36" height="22" fill="var(--green)"/><path d="M40 22h12l8 9v7H40z" fill="var(--green-dark)"/><circle cx="16" cy="42" r="5" fill="var(--navy)"/><circle cx="50" cy="42" r="5" fill="var(--navy)"/></svg><h4>Any Bin, Anytime, Anywhere</h4><p>We connect you with local companies Australia wide; for faster response times, less km's and emissions, greater reliability and lower prices</p></div>
  <div class="benefit"><svg class="icon" viewBox="0 0 66 50"><circle cx="33" cy="16" r="11" fill="var(--green)"/><path d="M14 48c0-12 8-18 19-18s19 6 19 18z" fill="var(--green-dark)"/></svg><h4>Service Guaranteed</h4><p>Want to speak to someone when it suits you? We answer the phones and return calls from 7.30am to 8pm 7 days a week</p></div>
  <div class="benefit"><svg class="icon" viewBox="0 0 66 50"><circle cx="38" cy="14" r="11" fill="none" stroke="var(--green)" stroke-width="3"/><path d="M6 38h20l10 6 24-10" fill="none" stroke="var(--navy)" stroke-width="3"/></svg><h4>Best Pricing</h4><p>We've done the hard work behind the scenes, so with one click you have your best priced, local skip</p></div>
  <div class="benefit"><svg class="icon" viewBox="0 0 66 50"><path d="M6 26l14-12 13 8 13-8 14 12-16 14-11-7-11 7z" fill="var(--green)"/></svg><h4>First Class Supply Partners</h4><p>Our local supply partners are the best in the business and share our passion for making you happy</p></div>
</div>

<section class="cta">
  <div class="cta-skyline" role="img" aria-label="City skyline silhouette"></div>
  <h2>We're ready to go!</h2>
  <div class="sub">To book, ask questions or just for a chat, call us 7 days a week, 7.30am to 8pm</div>
  <div class="label abs" style="top:178px;width:1200px;font-size:11px">QUICK QUOTE</div>
  <div class="search" style="left:342px;top:207px;width:562px">
    <div class="field">Enter postcode or suburb</div>
    <div class="go"><svg width="12" height="12" viewBox="0 0 12 12"><circle cx="5" cy="5" r="3.6" fill="none" stroke="#fff" stroke-width="1.8"/><path d="M8 8l3 3" stroke="#fff" stroke-width="1.8"/></svg>SEARCH</div>
  </div>
</section>
<svg class="footer-wave" viewBox="0 0 1200 100" preserveAspectRatio="none"><path d="M0 60 Q150 0 300 40 T620 50 T900 20 T1200 55 L1200 100 L0 100Z" fill="var(--footer)"/></svg>

<footer class="site-footer">
  <div class="foot-col" style="left:116px">Tipper Crate Rentals - Australia Wide<br>Sydney<br>Melbourne<br>Brisbane<br>Perth<br>Adelaide<br>Canberra</div>
  <div class="foot-col" style="left:444px">Learn More<br>Waste Types<br>Skip Bin Sizes<br>Refund Policy<br>Pay Later with FlexiPay<br>FAQ<br>Privacy</div>
  <div class="foot-col news" style="left:715px;top:26px"><h5>Latest Industry News<br>Sign up for the latest news, offers from<br>TIPPER CRATE RENTALS AUSTRALIA</h5></div>
  <div class="subscribe"><div class="field">Your email</div><div class="go">SUBSCRIBE</div></div>
  <div class="socials"><i></i><i></i><i></i><i></i></div>
</footer>
<div class="foot-bottom">
  <div class="abs" style="left:95px;top:40px">Copyright © 2019, TIPPER CRATE RENTALS AUSTRALIA. Powered by Storefront Co</div>
  <div class="pay"><i></i><i></i><i></i><i></i><i style="width:60px"></i></div>
</div>

</body>
</html>
```